Web Design Project

We need a design for the actual web.
http://mirela.vunto.example/
It will be a cakes and cupcakes online shop.

It is a one page site, with five anchors.

Inicio (Home)
Here it will show a brief explanation about our shop, just explaining we sell really nice cakes and cupcakes. Also we want to show a slide gallery, like the one it is working, but with not nice choosen pictures.

Productos/Tortas
This two anchors will be just one at the end, but I wanted to show the two options for accessing the different products, tabs or buttons. You can click on the firsts images on that links for see the "pop up image" with a better explanation of every product.

Contacto
Here it will show a little form, that will only appear in smartphones and maybe tablets, this form needs to be similar and much more simple than the principal form (the next anchor), so just focus on it once the next one its done.

Form
This will be the way the users will send the orders, its a complex form, focused on the UX. We dont want the user to type too much and we want it to surprise the user and fell really comfortable.

Industry/Entity Type

Tv

Requirements
Must have

• -Must have side menu, but you can redesign it completelly, but with the same structure
-Its important to focus all the content in the top and middle, we arent sure about users screens and it we set info at the footer, maybe its not gonna show (no scroll vertical).
-You can change all the colours of the site, we are open to new visions, you can surprise us.

```html
<!DOCTYPE html>
<html lang="es">
<head>
<meta charset="utf-8">
<title>Mirela Sweets</title>
<link rel="stylesheet" href="https://fonts.googleapis.com/css2?family=Fredoka:wght@500;600&family=Arimo:wght@400;700&display=swap">
<style>
:root{
  --navy:#0b2467;
  --navy-deep:#061a52;
  --navy-light:#1b3a8a;
  --salmon:#f2735c;
  --salmon-light:#f79a85;
  --sky:#8fcbe0;
  --sky-pale:#e6f4f8;
  --text:#4a4a4a;
  --rule:#e2e2e2;
  --page-bg:#dfeaf4;
}
*{margin:0;padding:0;box-sizing:border-box}
html,body{width:1200px;height:876px;overflow:hidden}
body{
  background:linear-gradient(90deg,#d3e3f0,var(--page-bg) 40%,var(--page-bg) 60%,#d3e3f0);
  font-family:"Arimo",Arial,sans-serif;color:var(--text);position:relative;
}
.sheet{position:absolute;left:150px;top:0;width:900px;height:876px;background:#fff;box-shadow:0 0 18px rgba(60,110,160,.35)}
.hero-cupcake{position:absolute;left:483px;top:0;width:234px;height:197px;border-radius:0 0 40px 40px;
  background:radial-gradient(ellipse at 50% 25%,#f7a3a8 0,#f4b7b4 35%,#e8c49a 60%,#fbf1e6 85%,#fff 100%)}
.brand{position:absolute;left:226px;top:44px;display:flex;align-items:center;gap:10px}
.brand-mark{width:14px;height:14px;background:var(--navy);display:block}
.brand-name{font-family:"Arimo",sans-serif;font-weight:700;font-size:26px;color:var(--navy);line-height:1}
.social{position:absolute;left:823px;top:45px;display:flex;align-items:center;gap:14px;font-size:10px;color:#999}
.social-link{display:flex;align-items:center;gap:5px;font-size:11px;font-weight:700;color:var(--navy-light);text-decoration:none}
.social-link i{width:12px;height:12px;background:var(--navy-light);display:block}
.social-link.alt{color:#2aa2d6}
.social-link.alt i{background:#2aa2d6}
.nav-ribbon{position:absolute;left:169px;top:125px;width:862px;height:47px}
.nav{position:absolute;left:211px;top:128px;width:778px;height:47px;background:linear-gradient(var(--navy-light),var(--navy) 40%,var(--navy-deep));
  display:flex;border-top:3px solid var(--navy-deep);border-bottom:4px solid var(--navy-deep)}
.nav a{flex:1;display:flex;align-items:center;justify-content:center;gap:7px;font-family:"Fredoka",sans-serif;font-weight:600;font-size:14px;color:#fff;text-decoration:none;letter-spacing:.4px;border-right:1px solid #2d4a96}
.nav a:last-child{border-right:0}
.hero{position:absolute;left:169px;top:198px;width:862px;height:281px;background:linear-gradient(90deg,#fff 50%,var(--sky-pale) 100%);overflow:hidden}
.hero-photo{position:absolute;left:0;top:0;width:431px;height:281px;background:radial-gradient(ellipse at 45% 55%,#f3dce2 0,#e9b7c4 40%,#f2e6dc 75%,#fff 100%)}
.hero-copy{position:absolute;left:469px;top:38px;width:342px}
.kicker{font-family:"Fredoka",sans-serif;font-weight:600;font-size:12px;letter-spacing:.5px}
.hero .kicker{color:var(--sky)}
.hero h1{font-family:"Fredoka",sans-serif;font-weight:600;font-size:36px;line-height:33px;color:var(--navy);margin-top:6px}
.hero p{font-size:11.5px;line-height:19px;text-align:justify;margin-top:19px}
.btn{display:inline-flex;align-items:center;gap:12px;height:27px;padding:0 18px 0 10px;background:linear-gradient(var(--salmon-light),var(--salmon));color:#fff;font-weight:700;font-size:12px;text-decoration:none;clip-path:polygon(0 0,90% 0,100% 50%,90% 100%,0 100%)}
.btn::after{content:"";border-left:4px solid #fff;border-top:3px solid transparent;border-bottom:3px solid transparent}
.hero .btn{margin-top:22px}
.cards{position:absolute;left:169px;top:498px;display:flex;gap:9.5px}
.card{width:165px;height:266px;border:1px solid var(--rule);padding:0 10px;position:relative}
.card.is-active{border-color:#b9dfec}
.card-photo{width:80px;height:88px;margin:12px auto 0;border-radius:40px 40px 10px 10px}
.card .kicker{color:var(--salmon-light);font-family:"Arimo",sans-serif;font-weight:700;font-size:11px;margin-top:10px}
.card h3{font-size:12.5px;line-height:16px;color:var(--navy);margin-top:7px;text-align:justify;text-align-last:left}
.card p{font-size:10.3px;line-height:17.5px;margin-top:4px;text-align:justify}
.card hr{border:0;border-top:1px solid var(--rule);margin-top:9px}
.card .btn{position:absolute;left:33px;bottom:15px;height:22px;font-size:11px;padding:0 22px 0 9px}
.card.is-active .btn{background:linear-gradient(#a9dff0,#5bbcdc)}
.promo{width:165px;height:266px;background:linear-gradient(#fde0da,#fcebe7 50%,#fcd9d2);text-align:center;padding:20px 11px 0;position:relative}
.promo .kicker{color:var(--salmon-light)}
.promo h2{font-family:"Fredoka",sans-serif;font-weight:600;font-size:22px;color:var(--salmon);margin-top:2px}
.promo-photo{width:140px;height:110px;margin:12px auto 0;border-radius:50%;background:radial-gradient(ellipse,#5a3224 0,#8a5a44 45%,#efd6cc 80%,transparent 100%)}
.promo p{text-align:justify;font-size:10.3px;line-height:17.5px;color:#b11d14;margin-top:13px}
.footer{position:absolute;left:169px;top:782px;width:862px;height:94px;background:linear-gradient(var(--navy),var(--navy-deep))}
.footer-nav{position:absolute;left:23px;top:27px;display:flex;font-size:11px;font-weight:700}
.footer-nav a{color:#8cc3ea;text-decoration:none}
.footer-nav span{color:#3b5aa0;margin:0 13px}
.copyright{position:absolute;left:23px;top:56px;font-size:10.5px;color:#8ea6d6}
.footer-brand{position:absolute;right:24px;top:34px;display:flex;align-items:center;gap:8px}
.footer-brand .brand-mark{background:#fff;width:11px;height:11px}
.footer-brand .brand-name{color:#fff;font-size:18px}
</style>
</head>
<body>
<div class="sheet"></div>
<div class="hero-cupcake" role="img" aria-label="Photo of a cupcake with pink frosting"></div>

<header class="brand">
  <i class="brand-mark"></i>
  <div class="brand-name">Mirela Sweets</div>
</header>

<div class="social">
  <span>Join us:</span>
  <a class="social-link" href="#"><i></i>Friendly</a>
  <a class="social-link alt" href="#"><i></i>Chirper</a>
</div>

<svg class="nav-ribbon" viewBox="0 0 862 47" aria-hidden="true">
  <polygon points="0,0 42,0 42,47 0,47 14,23" fill="#0b2467"/>
  <polygon points="862,0 820,0 820,47 862,47 848,23" fill="#0b2467"/>
  <line x1="4" y1="43" x2="42" y2="43" stroke="#2d4a96"/>
  <line x1="820" y1="43" x2="858" y2="43" stroke="#2d4a96"/>
</svg>
<nav class="nav">
  <a href="#inicio"><svg width="12" height="11" viewBox="0 0 12 11"><path d="M6 0 0 5h2v6h3V7h2v4h3V5h2z" fill="#fff"/></svg>INICIO</a>
  <a href="#productos">PRODUCTOS</a>
  <a href="#tortas">TORTAS</a>
  <a href="#contacto">CONTACTO</a>
  <a href="#form">FORM</a>
</nav>

<section class="hero" id="inicio">
  <div class="hero-photo" role="img" aria-label="Photo of decorated cupcakes on a pink cake stand"></div>
  <div class="hero-copy">
    <div class="kicker">TORTAS</div>
    <h1>LOREM IPSUM<br>DOLOR SIT AMET</h1>
    <p>Mauris vel velit eget lorem sodales lobortis ut lacinia neque. Donec id cursus tortor. Nullam eget ligula sed augue aliquet pharetra. Aenean egestas vestibulum leo.</p>
    <a class="btn" href="#">Read more</a>
  </div>
</section>

<section class="cards" id="productos">
  <article class="card is-active">
    <div class="card-photo" role="img" aria-label="Photo of a cupcake with sprinkles" style="background:linear-gradient(#f4c7d0,#f3b25a 55%,#e89a2c)"></div>
    <div class="kicker">CUPCAKES</div>
    <h3>Mauris vel velit eget lorem</h3>
    <p>Donec id cursus tortor. Nullam eget ligula sed augue aliquet pharetra.</p>
    <hr><a class="btn" href="#">View more</a>
  </article>
  <article class="card">
    <div class="card-photo" role="img" aria-label="Photo of a chocolate muffin" style="background:linear-gradient(#4a2c22,#2e1a14)"></div>
    <div class="kicker">CUPCAKES</div>
    <h3>Mauris vel velit eget lorem</h3>
    <p>Donec id cursus tortor. Nullam eget ligula sed augue aliquet pharetra.</p>
    <hr><a class="btn" href="#">View more</a>
  </article>
  <article class="card">
    <div class="card-photo" role="img" aria-label="Photo of an orange muffin in a paper case" style="background:linear-gradient(#f0a070,#e88a5a 55%,#eee)"></div>
    <div class="kicker">CUPCAKES</div>
    <h3>Mauris vel velit eget lorem</h3>
    <p>Donec id cursus tortor. Nullam eget ligula sed augue aliquet pharetra.</p>
    <hr><a class="btn" href="#">View more</a>
  </article>
  <article class="card" id="tortas">
    <div class="card-photo" role="img" aria-label="Photo of a chocolate cake topped with berries" style="background:linear-gradient(#7a3a2a,#4a2a1e 50%,#6b4a36)"></div>
    <div class="kicker">TORTAS</div>
    <h3>Mauris vel velit eget lorem</h3>
    <p>Donec id cursus tortor. Nullam eget ligula sed augue aliquet pharetra.</p>
    <hr><a class="btn" href="#">View more</a>
  </article>
  <aside class="promo">
    <div class="kicker">TORTAS</div>
    <h2>PROMOTION</h2>
    <div class="promo-photo" role="img" aria-label="Photo of a layered chocolate mousse cake"></div>
    <p>Donec id cursus tortor. Nullam eget ligula sed augue aliquet pharetra. &#9656;</p>
  </aside>
</section>

<footer class="footer" id="contacto">
  <nav class="footer-nav">
    <a href="#inicio">INICIO</a><span>|</span>
    <a href="#productos">PRODUCTOS</a><span>|</span>
    <a href="#tortas">TORTAS</a><span>|</span>
    <a href="#contacto">CONTACTO</a><span>|</span>
    <a href="#form">FORM</a>
  </nav>
  <div class="copyright">© Copyright 2012 Mirela Sweets. All Rights reserved.</div>
  <div class="footer-brand">
    <i class="brand-mark"></i>
    <div class="brand-name">Mirela Sweets</div>
  </div>
</footer>
</body>
</html>
```